Torvel, Inc. new buisness cards - brand guide included

We need new business cards. SLEAK SIMPLE FINANCE. They must include a place for NAME, TITLE, CELL, OFFICE PHONE, EMAIL. they also must include our services across the bottom. AIR, OCEAN, FTL, LTL, EXPRESS. for reference this will be being handed to some of the most prestigious shipping companies in a america.

Target Market(s)

Finance and corporate

Contact Information for Business Card

We need new business cards. SLEAK SIMPLE FINANCE. They must include a place for NAME, TITLE, CELL, OFFICE PHONE, EMAIL. they also must include our services across the bottom. AIR, OCEAN, FTL, LTL, EXPRESS.

Requirements
Must have
• We need new business cards. SLEAK SIMPLE FINANCE. They must include a place for NAME, TITLE, CELL, OFFICE PHONE, EMAIL. they also must include our services across the bottom. AIR, OCEAN, FTL, LTL, EXPRESS.
Nice to have
• USE THE COLORS AND LOGO IN THE BRAND GUIDE :)

```html
<!DOCTYPE html>
<html lang="en">
<head>
<meta charset="utf-8">
<title>Torvel, Inc. Business Cards</title>
<link rel="stylesheet" href="https://fonts.googleapis.com/css2?family=Tinos:ital,wght@0,400;0,700;1,400&display=swap">
<style>
  :root {
    --backdrop: #3b3b3b;
    --card-dark: #2e2e2e;
    --gold: #c8b99a;
    --white: #ffffff;
    --ink-dark: #2e2e2e;
  }
  * { margin: 0; padding: 0; box-sizing: border-box; }
  html, body { width: 1200px; height: 900px; overflow: hidden; }
  body {
    background: var(--backdrop);
    font-family: "Tinos", "Times New Roman", serif;
    display: flex;
    flex-direction: column;
    align-items: center;
    justify-content: center;
    gap: 60px;
  }
  .card {
    width: 560px;
    height: 320px;
    border-radius: 26px;
    position: relative;
    overflow: hidden;
  }

  /* Front */
  .card-front { background: var(--card-dark); }
  .front-name {
    position: absolute;
    top: 82px;
    left: 0;
    right: 0;
    text-align: center;
    color: var(--gold);
    font-size: 92px;
    font-weight: 400;
    letter-spacing: 2px;
    line-height: 1;
  }
  .services {
    position: absolute;
    left: 0;
    right: 0;
    bottom: 48px;
    display: flex;
    align-items: center;
    gap: 12px;
    color: var(--gold);
    font-size: 19px;
    letter-spacing: 0.5px;
  }
  .services .rule-start { width: 40px; height: 4px; background: var(--gold); margin-left: 30px; }
  .services .rule-end { flex: 1; height: 4px; background: var(--gold); margin-left: 6px; }
  .services .divider { margin: 0 2px; }

  /* Back */
  .card-back { background: var(--gold); display: flex; }
  .back-brand {
    width: 190px;
    background: var(--white);
    display: flex;
    align-items: center;
    justify-content: center;
  }
  .back-brand-name {
    color: var(--gold);
    font-size: 40px;
    letter-spacing: 1px;
  }
  .back-details {
    flex: 1;
    padding: 34px 0 0 34px;
    color: var(--white);
  }
  .person-name { font-size: 24px; font-weight: 700; letter-spacing: 0.5px; line-height: 1.1; }
  .person-title { font-size: 17px; font-style: italic; margin-bottom: 6px; }
  .contact-row {
    display: flex;
    align-items: flex-start;
    gap: 10px;
    font-size: 19px;
    line-height: 1.2;
    margin-bottom: 6px;
  }
  .contact-row.office { margin-bottom: 24px; }
  .contact-row.cell { font-weight: 700; }
  .contact-icon { width: 20px; height: 20px; flex: none; margin-top: 1px; }
</style>
</head>
<body>

  <section class="card card-front" aria-label="Business card front">
    <div class="front-name">Torvel</div>
    <div class="services">
      <span class="rule-start"></span>
      <span>AIR <span class="divider">|</span> OCEAN <span class="divider">|</span> FTL <span class="divider">|</span> LTL <span class="divider">|</span> EXPRESS</span>
      <span class="rule-end"></span>
    </div>
  </section>

  <section class="card card-back" aria-label="Business card back">
    <div class="back-brand"><span class="back-brand-name">Torvel</span></div>
    <div class="back-details">
      <div class="person-name">YOUR NAME</div>
      <div class="person-title">Designation</div>

      <div class="contact-row office">
        <svg class="contact-icon" viewBox="0 0 20 20"><circle cx="10" cy="10" r="10" fill="#fff"/><path d="M6.5 5.5l2 0 1 2.5-1.3 1a6 6 0 0 0 2.8 2.8l1-1.3 2.5 1v2a1 1 0 0 1-1 1A8 8 0 0 1 5.5 6.5a1 1 0 0 1 1-1z" fill="#c8b99a"/></svg>
        <span>312-555-0147</span>
      </div>

      <div class="contact-row cell">
        <svg class="contact-icon" viewBox="0 0 20 20"><circle cx="10" cy="10" r="10" fill="#fff"/><path d="M6.5 5.5l2 0 1 2.5-1.3 1a6 6 0 0 0 2.8 2.8l1-1.3 2.5 1v2a1 1 0 0 1-1 1A8 8 0 0 1 5.5 6.5a1 1 0 0 1 1-1z" fill="#c8b99a"/></svg>
        <span>312-555-0147</span>
      </div>

      <div class="contact-row email">
        <svg class="contact-icon" viewBox="0 0 20 20"><circle cx="10" cy="10" r="10" fill="#fff"/><rect x="5" y="6.5" width="10" height="7" fill="#c8b99a"/><path d="M5 6.5l5 4 5-4" fill="none" stroke="#fff" stroke-width="1"/></svg>
        <span>accounting@torvelinc.com</span>
      </div>

      <div class="contact-row address">
        <svg class="contact-icon" viewBox="0 0 20 20"><circle cx="10" cy="10" r="10" fill="#fff"/><path d="M10 4.5a3.5 3.5 0 0 0-3.5 3.5c0 2.6 3.5 7 3.5 7s3.5-4.4 3.5-7A3.5 3.5 0 0 0 10 4.5z" fill="#c8b99a"/><circle cx="10" cy="8" r="1.3" fill="#fff"/></svg>
        <span>4120 Harbor Point RD<br>Dunmore, DE19903</span>
      </div>
    </div>
  </section>

</body>
</html>
```